Consultancy company needs flyer design

We need a flyer design for a new service to be provided. It is a service in which project management is outsourced. Text of the service has been attached (in Dutch).
We would like the design to be in line with our website design (www.velostrin.com). Also we would like to re-use the main banner of the site (see attachment)

Industry/Entity Type

It Company

Requirements
Must have
• Flyer must be double sided

```html
<!DOCTYPE html>
<html lang="nl">
<head>
<meta charset="utf-8">
<title>Velostrin – PMAAS flyer</title>
<link rel="stylesheet" href="https://fonts.googleapis.com/css2?family=Lato:wght@400;700&family=Roboto+Condensed:wght@400;700&display=swap">
<style>
  :root {
    --bg: #e9e5df;
    --paper: #ffffff;
    --brown-dark: #6f5638;
    --brown: #7e6443;
    --gold: #a98b5f;
    --gold-line: #5e4930;
    --heading-dark: #4e3b24;
    --ink: #2a2622;
    --white: #ffffff;
    --steel-1: #1d2a36;
    --steel-2: #8fb0c8;
    --steel-3: #dfe9f0;
  }
  * { box-sizing: border-box; margin: 0; padding: 0; }
  html, body { width: 1200px; height: 1200px; overflow: hidden; background: var(--bg); }
  body { font-family: "Lato", sans-serif; color: var(--ink); }

  .flyer {
    position: absolute; left: 160px; top: 31px;
    width: 880px; height: 1138px;
    background: var(--paper); overflow: hidden;
    box-shadow: 0 4px 18px rgba(0,0,0,.18);
  }

  /* header */
  .brand { position: absolute; left: 51px; top: 29px; display: flex; align-items: center; gap: 10px; }
  .brand-square { width: 74px; height: 74px; border: 6px solid var(--brown); border-radius: 8px; }
  .brand-name { font: 700 38px/1 "Lato", sans-serif; color: var(--brown-dark); letter-spacing: -0.5px; }
  .header-band {
    position: absolute; right: 0; top: 87px; width: 550px; height: 27px;
    background: var(--brown);
    clip-path: polygon(26px 0, 100% 0, 100% 100%, 0 100%);
  }

  /* hero */
  .hero {
    position: absolute; left: 0; top: 117px; width: 880px; height: 354px;
    background:
      radial-gradient(circle at 78% 45%, var(--steel-3) 0 12%, var(--steel-2) 28%, transparent 46%),
      radial-gradient(circle at 30% 35%, var(--steel-3) 0 10%, var(--steel-2) 26%, transparent 44%),
      linear-gradient(135deg, #b9ccd9 0%, var(--steel-1) 45%, #6f8ea6 70%, #c9d8e2 100%);
  }
  .title-stripe {
    position: absolute; left: 405px; top: 469px; width: 475px; height: 31px;
    background: var(--brown-dark);
    clip-path: polygon(0 0, 100% 0, 100% 100%, 14px 100%);
  }
  .title-band {
    position: absolute; left: 0; top: 398px; width: 590px; height: 84px;
    background: var(--brown);
    clip-path: polygon(0 0, 548px 0, 100% 100%, 0 100%);
  }
  .title {
    position: absolute; left: 51px; top: 403px;
    font: 700 28.5px/36px "Roboto Condensed", sans-serif; color: var(--white);
  }

  /* body copy */
  .copy { position: absolute; left: 51px; width: 778px; font-size: 12.5px; line-height: 15.5px; text-align: justify; }
  .intro { top: 508px; }
  .checklist { list-style: none; top: 555px; text-align: left; }
  .checklist li { position: relative; padding-left: 21px; margin-bottom: 1.8px; }
  .checklist li::before {
    content: ""; position: absolute; left: 0; top: 2px; width: 11px; height: 11px;
    border: 1.5px solid var(--brown); border-radius: 2px;
  }
  .checklist li::after {
    content: ""; position: absolute; left: 4px; top: 0; width: 5px; height: 10px;
    border-right: 2px solid var(--brown); border-bottom: 2px solid var(--brown);
    transform: rotate(40deg);
  }
  .alternative { top: 650px; }

  /* services band */
  .services {
    position: absolute; left: 0; top: 732px; width: 880px; height: 233px;
    background: var(--gold);
  }
  .section-heading {
    position: absolute; left: 0; width: 880px; display: flex; align-items: center; justify-content: center; gap: 14px;
    font: 700 16px/1 "Roboto Condensed", sans-serif; color: var(--heading-dark); letter-spacing: .3px;
  }
  .section-heading::before, .section-heading::after {
    content: ""; height: 1px; width: 300px; background: var(--gold-line);
  }
  .heading-we { top: 9px; }
  .heading-you { top: 177px; }
  .col-divider { position: absolute; left: 450px; top: 36px; width: 1px; height: 192px; background: rgba(255,255,255,.25); }
  .ticks { position: absolute; list-style: none; font-size: 12.3px; line-height: 16px; color: #2d241a; }
  .ticks li { position: relative; padding-left: 21px; margin-bottom: 5px; text-align: justify; }
  .ticks li::before {
    content: ""; position: absolute; left: 0; top: 1px; width: 13px; height: 13px;
    border: 1.3px solid var(--white); border-radius: 50%;
  }
  .ticks li::after {
    content: ""; position: absolute; left: 5px; top: 3.5px; width: 3px; height: 6px;
    border-right: 1.5px solid var(--white); border-bottom: 1.5px solid var(--white);
    transform: rotate(40deg);
  }
  .ticks-left { left: 51px; top: 38px; width: 373px; }
  .ticks-right { left: 468px; top: 38px; width: 362px; }
  .ticks-right li { margin-bottom: 10px; }
  .ticks-you-left { left: 51px; top: 204px; width: 390px; }
  .ticks-you-right { left: 468px; top: 204px; width: 362px; }

  /* closing */
  .summary { top: 977px; }
  .pmo-heading { position: absolute; left: 51px; top: 1005px; font: 700 17px/1 "Roboto Condensed", sans-serif; color: var(--ink); }
  .pmo-text { top: 1029px; }

  /* footer */
  .footer-band {
    position: absolute; left: 0; top: 1093px; width: 690px; height: 29px;
    background: var(--brown);
    clip-path: polygon(0 0, 100% 0, 98.6% 100%, 0 100%);
  }
  .contact { position: absolute; top: 1100px; display: flex; align-items: center; gap: 7px; font-size: 13px; line-height: 15px; color: var(--white); }
  .contact-web { left: 51px; }
  .contact-mail { left: 357px; }
  .phone { position: absolute; left: 687px; top: 1092px; display: flex; align-items: center; gap: 7px;
    font: 400 19px/1 "Roboto Condensed", sans-serif; color: var(--ink); letter-spacing: .4px; }
</style>
</head>
<body>
<main class="flyer">
  <header>
    <div class="brand"><span class="brand-square"></span><span class="brand-name">velostrin</span></div>
    <div class="header-band"></div>
  </header>

  <div class="hero" role="img" aria-label="Close-up photograph of polished steel gears and cogwheels"></div>
  <div class="title-stripe"></div>
  <div class="title-band"></div>
  <h1 class="title">Ontzorging van uw projectdelivery:<br>Project Management As a Service (PMAAS)</h1>

  <p class="copy intro">U kunt voor de realisatie van uw projectportfolio de hulp inroepen van externe projectmanagers, en daarbij zelf de coördinatie verzorgen. Grote kans dat u dan tegen één of meer van de volgende zaken aan loopt:</p>
  <ul class="copy checklist">
    <li>Een wisselende kwaliteit van projectmanagers</li>
    <li>Problemen om kosten inzichtelijk en voorspelbaar of beheersbaar houden (management rapportage)</li>
    <li>Een ad hoc relatie met uw projectmanagers en leveranciers</li>
    <li>Beperkt leergedrag en herhaling van fouten</li>
    <li>Tijdverlies en kosten omdat u veel tijd kwijt bent aan uitleg van rand voorwaardelijke zaken</li>
  </ul>
  <p class="copy alternative">Een alternatief is onze PMAAS-service. Die bevat alle ingrediënten om uw projectenportfolio kostenefficiënt en op hoog kwaliteitsniveau te realiseren. Velostrin zorgt voor inzet van projectmanagers die al 'up to speed' zijn als ze bij u binnenkomen. Ze hebben de juiste expertise, zijn al ingewerkt op uw of onze standaard methodiek en op uw organisatorische setting. En heeft u ineens meer of minder werk? Geen probleem. Dan schalen wij net zo gemakkelijk op en af.</p>

  <section class="services">
    <h2 class="section-heading heading-we">WIJ ZORGEN VOOR</h2>
    <div class="col-divider"></div>
    <ul class="ticks ticks-left">
      <li>een eenduidige werkwijze, rapportering en gebruik van tooling</li>
      <li>een scherpe intake en voorbereidingsfase van de te starten projecten</li>
      <li>de benodigde op-en afschaling van project managers met het juiste profiel</li>
      <li>ingewerkte projectmanagers op de overeengekomen project methode</li>
    </ul>
    <ul class="ticks ticks-right">
      <li>continue monitoring op afgesproken KPI's over de projecten heen</li>
      <li>periodiek overleg over de performance</li>
      <li>continue verbetering op basis van klantevaluaties</li>
      <li>facturatie volgens afspraak (milestone-based)</li>
    </ul>
    <h2 class="section-heading heading-you">U ZORGT VOOR</h2>
    <ul class="ticks ticks-you-left"><li>een up to date forecast van de te realiseren projectportfolio</li></ul>
    <ul class="ticks ticks-you-right"><li>een goede projectbrief als basis voor onze intake</li></ul>
  </section>

  <p class="copy summary">Kortom: laat u ontzorgen in uw project delivery!</p>
  <h2 class="pmo-heading">PMO EN PPM</h2>
  <p class="copy pmo-text">Wilt u zich nog meer laten ontzorgen? Dat kan! Naast onze PMAAS-service leveren wij ook diensten op het gebied van Project Management Office (PMO) en/of Project Portfolio Management (PPM). Wij kunnen deze activiteiten voor u opzetten, maar ook de operationele aansturing ervan ondersteunen of voor onze rekening nemen.</p>

  <footer>
    <div class="footer-band"></div>
    <div class="contact contact-web">
      <svg width="15" height="15" viewBox="0 0 16 16" fill="none" stroke="#fff" stroke-width="1.2"><circle cx="8" cy="8" r="7"/><ellipse cx="8" cy="8" rx="3" ry="7"/><path d="M1 8h14M2.5 4.5h11M2.5 11.5h11"/></svg>
      <span>www.velostrin.com</span>
    </div>
    <div class="contact contact-mail">
      <svg width="18" height="13" viewBox="0 0 18 13" fill="none" stroke="#fff" stroke-width="1.4"><rect x="1" y="1" width="16" height="11" rx="1"/><path d="M1 1l8 6 8-6"/></svg>
      <span>info@velostrin.com</span>
    </div>
    <div class="phone">
      <svg width="31" height="31" viewBox="0 0 32 32" fill="none" stroke="#2a2622" stroke-width="1.8"><circle cx="16" cy="16" r="14"/><path d="M11 8c-2 1-3 3-2 6 1.5 4 4.5 7.5 8.5 9.5 2.5 1 4.5 0 5.5-1.5l-3-3-2 1c-2-1-4-3-5-5l1-2z" fill="#2a2622"/></svg>
      <span>085-0041927</span>
    </div>
  </footer>
</main>
</body>
</html>
```